Weightloss company needs Business Card

We want a business card that is clean and professional, yet portrays that we are a friendly, innovative, and versatile program designed to fit the needs of our clients.
I would like there to be 2 sides, one side having an appointment card, and the other side containing the logo and business information. There can be decorations on both sides. The logo is attached.

Target Market(s)

Men and women 40-60

Industry/Entity Type

Business

Contact Information for Business Card

Font styles to use
Sans Serif

Requirements
Must have
• The logo, space for business information
Nice to have
• The colors in the logo
Should not have
• No pictures of people or food

```html
<!DOCTYPE html>
<html lang="en">
<head>
<meta charset="UTF-8">
<title>Appointment Card</title>
<link href="https://fonts.googleapis.com/css2?family=Open+Sans:wght@400;700&display=swap" rel="stylesheet">
<style>
  :root {
    --card-red: #ff0030;
    --ring-cyan: #22d8ff;
    --panel-white: #ffffff;
    --text-red: #ff0030;
  }
  html, body {
    margin: 0;
    padding: 0;
    width: 1200px;
    height: 686px;
    overflow: hidden;
    background: var(--card-red);
  }
  .card {
    position: relative;
    width: 1200px;
    height: 686px;
    overflow: hidden;
    background: var(--card-red);
    font-family: "Open Sans", sans-serif;
    color: var(--text-red);
  }
  .card__oval {
    position: absolute;
    inset: 0;
  }
  .card__title {
    position: absolute;
    top: 48px;
    left: 0;
    width: 100%;
    margin: 0;
    text-align: center;
    font-size: 60px;
    font-weight: 700;
    line-height: 1;
  }
  .field {
    position: absolute;
    left: 199px;
    width: 800px;
    display: flex;
    align-items: flex-end;
    font-size: 50px;
    line-height: 1;
  }
  .field__label {
    margin-right: 4px;
  }
  .field__line {
    flex: 1;
    border-bottom: 3px solid var(--text-red);
    margin-bottom: 2px;
  }
  .field--name { top: 222px; }
  .field--extra { top: 332px; height: 52px; }
  .field--date { top: 442px; }
  .card__website {
    position: absolute;
    top: 580px;
    left: 0;
    width: 100%;
    text-align: center;
    font-size: 44px;
    line-height: 1;
  }
</style>
</head>
<body>
  <div class="card">
    <svg class="card__oval" width="1200" height="686" viewBox="0 0 1200 686" aria-hidden="true">
      <ellipse cx="600" cy="343" rx="523" ry="483" fill="var(--panel-white)" stroke="var(--ring-cyan)" stroke-width="28"/>
    </svg>

    <h1 class="card__title">Appointments</h1>

    <div class="field field--name">
      <span class="field__label">Name:</span>
      <span class="field__line"></span>
    </div>
    <div class="field field--extra">
      <span class="field__line"></span>
    </div>
    <div class="field field--date">
      <span class="field__label">Date:</span>
      <span class="field__line"></span>
    </div>

    <div class="card__website">www.risewellnessplan.com</div>
  </div>
</body>
</html>
```